Website Design for Brightfield Live: Sports TV for bars and restaurants

We need a website design for a streaming service called Brightfield Live. Brightfield Live provides sports programming to bars and restaurants across the United States and Canada. We would like to see a design that uses the colors of red, black, gold, and white. The final design should be functional business site, designed primarily for registration and ordering capabilities. In addition to a Registration and an Order page, we would like to see the following pages: Upcoming Events, FAQs, and About. We would also like to see an option at the top of the page to switch between languages (English and Spanish)

Target Market(s)

Male, 21-45 years old

Industry/Entity Type

Sports Bar

Number of Pages Required

5+ page

Font styles to use
Serif
Sans Serif

Requirements
Must have
• The project must have an easy to use registration page that include the following fields: Establishment's Name, Manager's name and contact info (phone number and email), and a field to upload a picture of their fire code. The project also must have an easy to use Upcoming events page with the ability to upload a fight's promotional poster.
Nice to have
• Nice to have an area on the main home page for testimonials and a scrolling ticker to put our partner's logos.

```html
<!DOCTYPE html>
<html lang="en">
<head>
<meta charset="utf-8">
<title>Brightfield Live – Sports Programming for Bars and Restaurants</title>
<link href="https://fonts.googleapis.com/css2?family=Michroma&family=Oswald:wght@400;500&family=Roboto:wght@400;500&display=swap" rel="stylesheet">
<style>
:root{
  --red:#c4000f;
  --red-dark:#8e0009;
  --red-card:#a8000d;
  --gold:#f3a712;
  --gold-light:#ffc21a;
  --black:#141414;
  --ink:#333;
  --white:#fff;
  --grey:#666;
}
*{box-sizing:border-box;margin:0;padding:0}
html,body{width:1200px;height:3066px;overflow:hidden}
body{position:relative;font-family:'Roboto',sans-serif;color:var(--ink);background:var(--white)}
.abs{position:absolute}
.display{font-family:'Michroma',sans-serif;letter-spacing:3px;text-transform:uppercase}

/* hero */
.hero{position:absolute;left:0;top:0;width:1200px;height:706px;overflow:hidden}
.hero-photo{position:absolute;inset:0;background:radial-gradient(ellipse at 30% 40%,#6a4a2e 0%,#3a2a1e 35%,#151210 75%),#1a1410}
.hero-shade{position:absolute;inset:0;background:linear-gradient(90deg,rgba(0,0,0,.45),rgba(0,0,0,.1) 60%,rgba(0,0,0,.3))}
.nav-bar{position:absolute;top:65px;height:50px}
.nav-bar ul{list-style:none;display:flex;height:100%;align-items:center}
.nav-bar a{color:var(--white);text-decoration:none;font:500 16px 'Roboto',sans-serif;text-transform:uppercase;padding:0 18px}
.nav-left{left:118px;width:420px}
.nav-right{left:660px;width:420px}
.nav-shape{position:absolute;inset:0}
.nav-bar ul{position:relative}
.nav-right ul{padding-left:60px}
.logo{position:absolute;left:540px;top:24px;width:120px;height:140px;display:flex;flex-direction:column;align-items:center;justify-content:center;color:var(--white);font:500 26px/1 'Oswald',sans-serif;text-transform:uppercase;text-align:center}
.hero-title{position:absolute;left:118px;top:342px;color:var(--white);font-size:33px;line-height:37px}
.quick-reg{position:absolute;left:732px;top:188px;width:348px;height:380px;background:var(--red);border:2px solid #e0303a;padding:20px 28px}
.quick-reg h2{color:var(--white);font-size:17px;letter-spacing:3px;text-align:center;margin-bottom:16px}
.field{height:40px;border:1px solid #e8555c;background:var(--red-dark);color:var(--white);font-size:13px;display:flex;align-items:center;justify-content:space-between;padding:0 16px;margin-bottom:10px}
.btn-gold{background:linear-gradient(var(--gold-light),var(--gold));color:var(--white);font:500 18px 'Oswald',sans-serif;text-transform:uppercase;display:flex;align-items:center;justify-content:center;text-decoration:none}
.quick-reg .btn-gold{height:46px;margin-top:6px}
.partners{position:absolute;left:100px;top:630px;width:1000px;height:50px;display:flex;align-items:center;justify-content:space-between}
.partner-badge{width:110px;height:32px;background:rgba(255,255,255,.85);border-radius:4px}
.partner-badge.round{width:40px;border-radius:50%}
.arrow{color:var(--white);font-size:26px}

/* about */
.about-photo{position:absolute;left:112px;top:760px;width:430px;height:405px}
.about-text{position:absolute;left:613px;top:800px;width:470px}
.about-text h2{font-size:24px;line-height:34px;color:var(--black)}
.about-text h2 span{color:var(--red);display:block}
.about-text p{font-size:13.5px;line-height:23px;color:var(--grey);margin-top:22px}
.about-text .btn-gold{width:166px;height:44px;margin-top:34px;font-size:17px}

/* blogs */
.blogs{position:absolute;left:0;top:1210px;width:1200px;height:600px;background:var(--red)}
.section-title{position:absolute;left:0;width:1200px;text-align:center;font-size:22px}
.blogs .section-title{top:44px;color:var(--white)}
.blog-card{position:absolute;top:190px;width:282px;height:276px;background:var(--red-card);color:var(--white);text-align:center;padding-top:140px}
.blog-photo{position:absolute;left:35px;top:-102px;width:212px;height:212px;border-radius:50%}
.blog-card .date{font-size:13px}
.blog-card h3{font:400 21px 'Roboto',sans-serif;margin:14px 0 8px}
.blog-card p{font-size:12.5px;line-height:20px;padding:0 30px}

/* testimonials */
.testimonials{position:absolute;left:0;top:1720px;width:1200px;height:396px}
.testimonials .section-title{top:92px;color:var(--white)}
.avatar-ring{position:absolute;left:212px;top:155px;width:148px;height:148px;border-radius:50%;border:3px solid #fff3;background:var(--white);padding:5px}
.avatar{width:100%;height:100%;border-radius:50%;background:radial-gradient(circle at 50% 40%,#9ab6d2,#4c7aa6)}
.divider{position:absolute;left:390px;top:160px;width:1px;height:138px;background:#ffffff80}
.quote{position:absolute;left:420px;top:160px;width:560px;color:var(--white);font-style:italic;font-size:15px;line-height:29px}
.quote-mark{font:500 40px/0 'Oswald',sans-serif;font-style:normal;vertical-align:-14px;margin:0 6px}
.author{position:absolute;left:455px;top:275px;color:var(--white);font-size:13px;text-transform:uppercase}
.dots{position:absolute;left:540px;top:335px;display:flex;gap:6px;align-items:center}
.dots span{width:9px;height:9px;border-radius:50%;background:#ffffff90}
.dots .active{background:var(--white)}
.dots .nav{width:20px;height:20px;background:var(--white);color:var(--black);font-size:12px;display:flex;align-items:center;justify-content:center}

/* faq */
.faq{position:absolute;left:0;top:2116px;width:1200px;height:620px;overflow:hidden}
.faq-photo{position:absolute;inset:0;background:linear-gradient(120deg,#c9b9a4,#e8ddcf 40%,#b99d7e 75%,#8e7a66)}
.faq .section-title{top:88px;color:var(--black)}
.faq-list{position:absolute;left:278px;top:142px;width:642px}
.faq-item{height:42px;background:var(--white);margin-bottom:7px;display:flex;align-items:center;justify-content:space-between;padding:0 12px 0 18px;font-size:14px;border-bottom:3px solid #ddd}
.toggle{width:26px;height:26px;border-radius:50%;background:var(--red);color:var(--white);display:flex;align-items:center;justify-content:center;font-size:20px;line-height:1}
.faq-item.open{background:var(--red-dark);color:var(--white);border:0;margin-bottom:0}
.faq-answer{background:var(--white);padding:14px 34px 22px;font-size:12px;line-height:20px;color:var(--grey)}
.ridge{position:absolute;left:0;bottom:0;width:1200px;height:110px}

/* footer */
.footer{position:absolute;left:0;top:2670px;width:1200px;height:328px;background:var(--black);color:#ddd}
.footer .logo{left:139px;top:48px;height:154px;font-size:28px}
.footer-col{position:absolute;top:60px}
.footer-col h4{font-family:'Michroma',sans-serif;font-size:14px;letter-spacing:3px;color:var(--white);text-transform:uppercase;font-weight:400;margin-bottom:20px}
.footer-col ul{list-style:none;font-size:13.5px}
.footer-col li{margin-bottom:11px}
.blog-links li::before{content:"›";font-size:20px;margin-right:6px;color:var(--white)}
.social li{display:flex;align-items:center;gap:10px;margin-bottom:12px}
.social i{width:26px;height:26px;border-radius:50%;background:#3b5c9e;display:inline-block}
.social li:nth-child(2) i{background:#3aa3e0}
.social li:nth-child(3) i{background:#1b78b5}
.social li:nth-child(4) i{background:#d6422f}
.copyright{position:absolute;left:0;top:2998px;width:1200px;height:68px;background:#0a0a0a;color:#999;font-size:13px;display:flex;align-items:center;justify-content:center}
</style>
</head>
<body>

<header class="hero">
  <div class="hero-photo" role="img" aria-label="Fans cheering while watching a game in a dimly lit sports bar"></div>
  <div class="hero-shade"></div>

  <nav class="nav-bar nav-left">
    <svg class="nav-shape" viewBox="0 0 420 50" preserveAspectRatio="none">
      <polygon points="20,0 420,0 420,50 0,50" fill="#f3a712"/>
      <polygon points="20,0 136,0 116,50 0,50" fill="#c4000f"/>
    </svg>
    <ul><li><a href="#">Home</a></li><li><a href="#">About</a></li><li><a href="#">Upcoming Events</a></li></ul>
  </nav>
  <nav class="nav-bar nav-right">
    <svg class="nav-shape" viewBox="0 0 420 50" preserveAspectRatio="none">
      <polygon points="0,0 420,0 400,50 0,50" fill="#f3a712"/>
    </svg>
    <ul><li><a href="#">Register</a></li><li><a href="#">FAQ</a></li><li><a href="#">Contact Us</a></li></ul>
  </nav>
  <div class="logo"><span>Brightfield</span><span>Live</span></div>

  <h1 class="hero-title display">Sports<br>programming to<br>bars and<br>restaurants</h1>

  <form class="quick-reg">
    <h2 class="display">Quick Registration</h2>
    <div class="field">Establishment's Name</div>
    <div class="field">Manager's name</div>
    <div class="field">Phone</div>
    <div class="field">Email</div>
    <div class="field">Upload a picture
      <svg width="16" height="14" viewBox="0 0 16 14"><path d="M9 0l7 6-7 6V8C4 8 1 10 0 14 0 8 3 4 9 4z" fill="#fff"/></svg>
    </div>
    <a class="btn-gold" href="#">Submit</a>
  </form>

  <div class="partners">
    <span class="arrow">‹</span>
    <span class="partner-badge"></span>
    <span class="partner-badge"></span>
    <span class="partner-badge"></span>
    <span class="partner-badge"></span>
    <span class="partner-badge"></span>
    <span class="partner-badge"></span>
    <span class="arrow">›</span>
  </div>
</header>

<section>
  <svg class="about-photo" viewBox="0 0 430 405">
    <polygon points="108,2 322,2 428,202 322,403 108,403 2,202" fill="none" stroke="#f3a712" stroke-width="3"/>
    <polygon points="118,18 312,18 410,202 312,387 118,387 20,202" fill="#6b4a3a" role="img" aria-label="Three friends cheering with beer mugs at a bar"/>
  </svg>
  <div class="about-text">
    <h2 class="display">About<span>Brightfield Live</span></h2>
    <p>Morbi eget arcu Morbi porta libero id ullamcorper nonummy nibh ligula pulvinar metus eget consectetuer augue nisi quis lacus Ut ac mi quis lacus mollis aliquam Curabitur iaculis tempus eros</p>
    <p>Curabitur vel mi sit amet magna malesuada ultrices Ut nisi erat fermentum vel congue id euismod in elit Fusce ultricies orci</p>
    <a class="btn-gold" href="#">Read More</a>
  </div>
</section>

<section class="blogs">
  <h2 class="section-title display">Our Blogs</h2>
  <article class="blog-card" style="left:157px">
    <div class="blog-photo" role="img" aria-label="Friends toasting beers at a sports bar" style="background:radial-gradient(circle,#b56a3a,#4a2a1c)"></div>
    <div class="date">25 JUNE 2018</div><h3>Blog Title here</h3>
    <p>Class aptent taciti sociosqu ad litora torquent per conubia nostra</p>
  </article>
  <article class="blog-card" style="left:460px">
    <div class="blog-photo" role="img" aria-label="Man smiling with a drink in a bar" style="background:radial-gradient(circle,#4a5ab5,#1c1f4a)"></div>
    <div class="date">25 JUNE 2018</div><h3>Blog Title here</h3>
    <p>Class aptent taciti sociosqu ad litora torquent per conubia nostra</p>
  </article>
  <article class="blog-card" style="left:767px">
    <div class="blog-photo" role="img" aria-label="Fans raising glasses in front of a big screen" style="background:radial-gradient(circle,#6a7a6a,#1e2420)"></div>
    <div class="date">25 JUNE 2018</div><h3>Blog Title here</h3>
    <p>Class aptent taciti sociosqu ad litora torquent per conubia nostra</p>
  </article>
</section>

<section class="testimonials">
  <svg class="abs" style="left:0;top:0" width="1200" height="396" viewBox="0 0 1200 396">
    <path d="M0,80 Q600,-15 1200,80 L1200,396 L0,396 Z" fill="#f3a712"/>
  </svg>
  <h2 class="section-title display">Testimonials</h2>
  <div class="avatar-ring"><div class="avatar" role="img" aria-label="Customer portrait"></div></div>
  <div class="divider"></div>
  <p class="quote"><span class="quote-mark">“</span>Vivamus porttitor purus nisi eleifend libero a tempus libero lectus feugiat felis Morbi diam mauris viverra in gravida eu mattis in ante Morbi eget arcu Morbi porta libero id ullamcorper nonummy nibh<span class="quote-mark">”</span></p>
  <div class="author">By Author Name</div>
  <div class="dots"><span class="nav">‹</span><span class="active"></span><span></span><span></span><span></span><span class="nav">›</span></div>
</section>

<section class="faq">
  <div class="faq-photo" role="img" aria-label="Blurred interior of a busy restaurant"></div>
  <h2 class="section-title display">FAQ</h2>
  <div class="faq-list">
    <div class="faq-item">Q: Morbi diam mauris viverra in gravida eu mattis in ante ?<span class="toggle">+</span></div>
    <div class="faq-item">Q: Morbi eget arcu Morbi porta libero id ullamcorper ?<span class="toggle">+</span></div>
    <div class="faq-item">Q: Nonummy nibh ligula pulvinar metus eget ?<span class="toggle">+</span></div>
    <div class="faq-item open">Q: Eonsectetuer augue nisi quis lacus ?<span class="toggle">−</span></div>
    <div class="faq-answer">Vivamus porttitor purus nisi eleifend libero a tempus libero lectus feugiat felis Morbi diam mauris viverra in gravida eu mattis in ante Morbi eget arcu Morbi porta libero id ullamcorper nonummy nibh ligula pulvinar metus eget consectetuer augue nisi quis lacus Ut ac mi quis</div>
  </div>
  <svg class="ridge" viewBox="0 0 1200 110" preserveAspectRatio="none">
    <polygon points="0,60 90,40 170,70 260,30 350,55 430,35 520,65 610,25 700,50 790,20 860,45 950,15 1040,40 1120,20 1200,35 1200,110 0,110" fill="#141414"/>
  </svg>
</section>

<footer class="footer">
  <div class="logo"><span>Brightfield</span><span>Live</span></div>
  <div class="footer-col" style="left:370px">
    <h4>Quick Links</h4>
    <ul><li>Home</li><li>About</li><li>Upcoming Events</li><li>Register</li><li>FAQ</li><li>Contact us</li></ul>
  </div>
  <div class="footer-col" style="left:593px">
    <h4>Latest Blogs</h4>
    <ul class="blog-links"><li>Vivamus porttitor purus nisi</li><li>Eleifend libero a tempus libero lectus</li><li>Feugiat felis Morbi diam</li><li>Mauris viverra in gravida</li><li>Eu mattis in ante Morbi eget arcu</li></ul>
  </div>
  <div class="footer-col" style="left:910px">
    <h4>Follow Us</h4>
    <ul class="social"><li><i></i>Friendpage</li><li><i></i>Chirpline</li><li><i></i>WorkNet</li><li><i></i>Circleplus</li></ul>
  </div>
</footer>
<div class="copyright">© 2018 Brightfield Live&nbsp; All right reserved&nbsp; Term of Use</div>

</body>
</html>
```